Broschüren-Design für Schuhmanufaktur
Zielgruppe
Schuhmanufaktur für Maßschuhe möchte sich modernisieren.
Aufgabenstellung
Maße und andere Daten entnehmen Sie sich den angefügten Daten und Bildern.
Es soll eine Broschüre (Maße etc in daten und skizze) und ein Plakat mit composing erstellt werden.
Offene Daten erwünscht (.ai)

```html
<!DOCTYPE html>
<html lang="de">
<head>
<meta charset="utf-8">
<title>Schuhmanufaktur Feinschritt – Plakat und Broschüre</title>
<link href="https://fonts.googleapis.com/css2?family=Quicksand:wght@300;500;700&family=Open+Sans:wght@400;600&display=swap" rel="stylesheet">
<style>
:root{
  --canvas:#efefef;
  --ink-dark:#2e2d2c;
  --ink-brown:#33241f;
  --band:rgba(120,78,40,.72);
  --band-strong:rgba(92,58,30,.8);
  --label:#6b3f1c;
  --white:#ffffff;
  --muted:#cfc7c2;
  --autumn-a:#c8913f;
  --autumn-b:#6d4a2a;
  --leather-a:#b8692a;
  --leather-b:#4a2b18;
}
*{box-sizing:border-box;margin:0;padding:0}
html,body{width:1200px;height:848px;overflow:hidden;background:var(--canvas)}
body{position:relative;font-family:"Open Sans",sans-serif;color:var(--white)}
.sheet{position:absolute;overflow:hidden;box-shadow:0 2px 8px rgba(0,0,0,.18)}
.photo{position:absolute}
.photo--autumn{background:linear-gradient(160deg,var(--autumn-a) 0%,#8a6a48 40%,#3b3432 70%,var(--autumn-b) 100%)}
.photo--leather{background:linear-gradient(150deg,#5a3a22 0%,var(--leather-a) 45%,var(--leather-b) 100%)}
.photo--pavement{background:linear-gradient(160deg,#6d7a86 0%,var(--leather-a) 50%,#8a4a1c 80%,#56636e 100%)}
.photo--loafer{background:linear-gradient(140deg,#2f4d50 0%,#9c7b52 55%,#2c4346 100%)}

/* Plakat & Titelseite */
.title-band{position:absolute;left:7%;font-family:"Quicksand",sans-serif;line-height:1;white-space:nowrap}
.title-band__top{display:inline-block;background:var(--band);font-weight:300;padding:.08em .2em}
.title-band__main{display:inline-block;background:var(--band-strong);font-weight:700;padding:.05em .15em;margin-top:.08em}
.wordmark{position:absolute;display:flex;align-items:center;gap:6px;font-family:"Quicksand",sans-serif;font-weight:500;color:var(--white)}
.wordmark__dot{width:14px;height:14px;border-radius:50%;background:var(--white)}

.poster{left:40px;top:40px;width:380px;height:380px}
.poster .title-band{top:56px}
.poster .title-band__top{font-size:34px}
.poster .title-band__main{font-size:56px}
.poster .wordmark{right:14px;bottom:22px;font-size:18px}

.back-panel{left:450px;top:40px;width:350px;height:350px;background:var(--ink-dark);padding:110px 0 0 40px;font-family:"Open Sans",sans-serif}
.back-panel__firm{font-weight:600;font-size:11px}
.back-panel p{font-size:9.5px;line-height:1.45;color:var(--muted)}
.back-panel .gap{margin-top:12px}
.cover-panel{left:800px;top:40px;width:350px;height:350px}
.cover-panel .title-band{top:54px}
.cover-panel .title-band__top{font-size:31px}
.cover-panel .title-band__main{font-size:51px}
.cover-panel .wordmark{right:14px;bottom:20px;font-size:16px}

/* Innenseiten */
.strip{top:440px;width:200px;height:370px;background:var(--ink-dark)}
.strip__head{position:relative;height:120px}
.strip__head .label{position:absolute;left:6px;bottom:6px}
.label{font-family:"Quicksand",sans-serif;font-weight:500;font-size:13px;background:rgba(50,30,20,.55);padding:1px 5px;color:var(--white)}
.service{height:83px;padding:9px 12px;background:linear-gradient(180deg,var(--ink-brown),#1e1816)}
.service:nth-child(3){background:linear-gradient(180deg,#3a3735,#231f1d)}
.service h3{font-family:"Quicksand",sans-serif;font-size:10px;font-weight:700;margin-bottom:4px}
.service p,.shoe p,.intro p{font-size:7.5px;line-height:1.4;color:var(--muted)}

.services{left:40px}
.lineup{left:273px;top:440px;width:420px;height:370px;background:var(--ink-dark)}
.lineup__head{position:relative;height:110px}
.lineup__head .label{position:absolute;left:8px;bottom:8px;font-size:15px}
.lineup__grid{display:grid;grid-template-columns:1fr 1fr;grid-template-rows:repeat(3,1fr);height:260px}
.shoe{position:relative;padding:8px 10px;border-top:1px solid #4a3a34}
.shoe:nth-child(odd){background:#3a2b26}
.shoe__thumb{width:44px;height:30px;margin-bottom:5px}
.shoe__name{position:absolute;left:60px;top:24px;font-family:"Quicksand",sans-serif;font-size:8px;font-weight:700;background:var(--label);padding:1px 5px}
.shoe--loafer-photo{padding:0}
.shoe--loafer-photo .photo{inset:0}

.craft{left:726px}
.craft .photo{left:0;top:0;width:200px;height:250px}
.craft__claim{position:absolute;left:6px;top:218px;font-family:"Quicksand",sans-serif;font-weight:700;font-size:12px;line-height:1.15}
.craft__claim span{display:inline-block;background:rgba(50,30,20,.6);padding:0 4px}
.craft__foot{position:absolute;left:0;top:250px;width:200px;height:120px;background:linear-gradient(180deg,#3b3735,#1c1a19)}

.intro{left:960px;padding:22px 14px;background:linear-gradient(180deg,#3a3735,#1d1b1a)}
.intro h2{font-family:"Quicksand",sans-serif;font-size:11px;font-weight:700;line-height:1.25;margin-bottom:10px}
.intro p{margin-bottom:8px;font-size:8px}
</style>
</head>
<body>

<section class="sheet poster" aria-label="Plakat">
  <div class="photo photo--autumn" style="inset:0" role="img" aria-label="Foto: Herrenbeine in Budapester Schuhen mit altem Lederkoffer auf Herbstlaub"></div>
  <div class="title-band">
    <span class="title-band__top">Schuhmanufaktur</span><br>
    <span class="title-band__main">Feinschritt</span>
  </div>
  <div class="wordmark"><span class="wordmark__dot"></span>Feinschritt</div>
</section>

<section class="sheet back-panel" aria-label="Broschüre Rückseite">
  <p class="back-panel__firm">Schuhmanufaktur Feinschritt GmbH</p>
  <p>Lina Varga und Teo Marelli</p>
  <p>Lindenweg 12</p>
  <p>50667 Köln-Altstadt</p>
  <p class="gap">Tel: 0221 480-116</p>
  <p>Fax: 0221 480-117</p>
  <p class="gap">kontakt@schuhmanufaktur-feinschritt.de</p>
  <p class="gap" style="color:var(--white);font-weight:600">www.schuhmanufaktur-feinschritt.de</p>
</section>

<section class="sheet cover-panel" aria-label="Broschüre Titelseite">
  <div class="photo photo--autumn" style="inset:0" role="img" aria-label="Foto: Herrenbeine in Budapester Schuhen mit altem Lederkoffer auf Herbstlaub"></div>
  <div class="title-band">
    <span class="title-band__top">Schuhmanufaktur</span><br>
    <span class="title-band__main">Feinschritt</span>
  </div>
  <div class="wordmark"><span class="wordmark__dot"></span>Feinschritt</div>
</section>

<section class="sheet strip services" aria-label="Leistungen">
  <div class="strip__head">
    <div class="photo photo--leather" style="inset:0" role="img" aria-label="Foto: zwei Paar hellbraune Budapester auf Holzboden"></div>
    <span class="label">Leistungen</span>
  </div>
  <div class="service"><h3>Reparieren</h3><p>Ein abgelöster Absatz oder eine gerissene Naht? Wir bringen Ihre Lieblingsschuhe wieder in Form.</p></div>
  <div class="service"><h3>Verbessern</h3><p>Wir passen Schuhe an Ihren Fuß an, polstern nach und ersetzen Sohlen.</p></div>
  <div class="service"><h3>Kreieren</h3><p>Nach Maß gefertigte Modelle, ganz nach Ihren Wünschen und Ihrer Form.</p></div>
</section>

<section class="sheet lineup" aria-label="Klassische Hauptdarsteller">
  <div class="lineup__head">
    <div class="photo photo--leather" style="inset:0" role="img" aria-label="Foto: drei Lederschuhe in Braun und Schwarz nebeneinander"></div>
    <span class="label">Klassische Hauptdarsteller</span>
  </div>
  <div class="lineup__grid">
    <div class="shoe"><div class="shoe__thumb photo--leather" style="background:linear-gradient(140deg,#222,#5a3a22)" role="img" aria-label="Foto: Oxford-Schuh"></div><span class="shoe__name">OXFORD</span><p>Der geschlossene Schnürer für feine Anlässe.</p></div>
    <div class="shoe"><div class="shoe__thumb photo--leather" role="img" aria-label="Foto: Monk-Schuh"></div><span class="shoe__name">MONK</span><p>Mit Schnalle statt Schnürung, elegant und bequem.</p></div>
    <div class="shoe"><div class="shoe__thumb photo--leather" style="background:linear-gradient(140deg,#c9a57a,#8a5a2a)" role="img" aria-label="Foto: Chelsea Boot"></div><span class="shoe__name">CHELSEA BOOT</span><p>Schlupfstiefel mit elastischem Einsatz an der Seite.</p></div>
    <div class="shoe"><div class="shoe__thumb photo--leather" style="background:linear-gradient(140deg,#3a2020,#7a3a2a)" role="img" aria-label="Foto: Budapester"></div><span class="shoe__name">BUDAPESTER</span><p>Robuster Lochmusterschuh mit markanter Kappe.</p></div>
    <div class="shoe"><div class="shoe__thumb photo--leather" style="background:linear-gradient(140deg,#5a4030,#a0724a)" role="img" aria-label="Foto: Loafer"></div><span class="shoe__name">LOAFER</span><p>Leichter Slipper für entspannte Tage.</p></div>
    <div class="shoe shoe--loafer-photo"><div class="photo photo--loafer" role="img" aria-label="Foto: Wildleder-Loafer auf türkisem Untergrund"></div></div>
  </div>
</section>

<section class="sheet strip craft" aria-label="Lederhandwerk aus Leidenschaft">
  <div class="photo photo--pavement" role="img" aria-label="Foto: ein Paar glänzende cognacfarbene Oxford-Schuhe auf Pflaster"></div>
  <div class="craft__claim"><span>Lederhandwerk</span><br><span>aus Leidenschaft</span></div>
  <div class="craft__foot"></div>
</section>

<section class="sheet strip intro" aria-label="Über uns">
  <h2>Schuhmanufaktur<br>Feinschritt</h2>
  <p>Seit 2013 fertigen wir in unserer kleinen Werkstatt Maßschuhe, die ein Leben lang begleiten.</p>
  <p>Jedes Paar entsteht in Handarbeit aus ausgesuchtem Leder.</p>
  <p>Wir freuen uns auf Ihren Besuch.</p>
</section>

</body>
</html>
```